Stitchwell Studio

I'd like to have a website made in squarespace that is as close as possible to another website already on the internet. The website address of the website I'd like to base it on is: https://www.brimfeltmending.example.au

Target Market(s)

People looking for clothing alterations

Coding

Coded - Design and coding required

Number of Pages Required

1 page

Colors

Designer to choose colors to be used in the design.

Requirements
Must have
• Must be made in squarespace with a layout identical to this website: https://www.brimfeltmending.example.au

```html
<!DOCTYPE html>
<html lang="en">
<head>
<meta charset="utf-8">
<title>Stitchwell Studio — Clothing Alterations</title>
<link rel="stylesheet" href="https://fonts.googleapis.com/css2?family=Tinos&family=Lato:wght@400;700&display=swap">
<style>
:root{
  --teal:#16333b;
  --teal-deep:#112a31;
  --tan:#d9b79b;
  --tan-soft:#e6cdb8;
  --ink:#333;
  --muted:#666;
  --line:#cfd4d6;
  --white:#fff;
  --serif:"Tinos","Times New Roman",serif;
  --sans:"Lato",Arial,sans-serif;
}
*{box-sizing:border-box;margin:0;padding:0}
html,body{width:1200px;height:3485px;overflow:hidden}
body{position:relative;background:var(--white);font-family:var(--sans);color:var(--ink)}
.abs{position:absolute}

/* header */
.site-header{position:absolute;left:0;top:0;width:1200px;height:96px;background:var(--white)}
.brand{position:absolute;left:120px;top:18px;width:132px;text-align:center}
.brand-mark{display:block;width:34px;height:34px;margin:0 auto 4px;border:1.5px solid var(--teal);border-radius:50%}
.brand-name{font-family:var(--serif);font-size:13px;color:var(--teal);letter-spacing:.2px;white-space:nowrap}
.main-nav{position:absolute;top:46px;left:361px;display:flex;gap:0}
.main-nav a{font-family:var(--serif);font-size:13px;color:var(--ink);text-decoration:none;margin-right:26px;text-transform:uppercase}
.main-nav a.is-active{color:var(--tan)}
.header-call{position:absolute;left:920px;top:34px;display:flex;align-items:center;gap:10px}
.header-call-text{font-family:var(--serif);font-size:14px;color:#555;line-height:17px}
.header-call-text span{display:block;font-size:13px;color:var(--tan)}

/* hero */
.hero{position:absolute;left:0;top:96px;width:1200px;height:649px;
  background:linear-gradient(115deg,#5a3c26 0%,#8a5a34 25%,#c98a4a 38%,#6e6b70 60%,#8e949e 100%)}
.hero-title{position:absolute;left:0;top:248px;width:1200px;text-align:center;font-family:var(--serif);
  font-size:40px;line-height:46px;color:var(--white);text-transform:uppercase}
.btn{position:absolute;display:flex;align-items:center;justify-content:center;border-radius:30px;
  font-family:var(--serif);font-size:14px;text-transform:uppercase;text-decoration:none}
.btn-tan{background:var(--tan);color:var(--teal)}
.btn-white{background:var(--white);color:var(--teal)}
.btn-teal{background:var(--teal);color:var(--white)}
.hero-arrow{position:absolute;top:288px}
.hero-dots{position:absolute;top:612px;left:564px;display:flex;gap:13px}
.hero-dots i{width:9px;height:9px;border-radius:50%;background:var(--teal)}
.hero-dots i:first-child{background:#b9b3ad}

/* about & offers split panels */
.panel{position:absolute;left:0;width:1200px;background:var(--teal)}
.panel-title{position:absolute;left:120px;font-family:var(--serif);font-size:32px;color:var(--white);font-weight:400}
.panel-text{position:absolute;left:120px;width:420px;font-size:12.5px;line-height:21px;color:var(--white)}
.photo{position:absolute}

/* services */
.services-heading{position:absolute;left:117px;top:1236px;font-family:var(--serif);font-size:30px;line-height:39px;color:var(--ink);font-weight:400}
.service{position:absolute;width:225px}
.service-icon{width:56px;height:52px;border-radius:6px;background:linear-gradient(160deg,var(--tan-soft),var(--tan))}
.service-title{margin-top:44px;font-family:var(--serif);font-size:18px;color:var(--ink);font-weight:400}
.service-text{margin-top:18px;font-size:12px;line-height:21px;color:var(--muted)}

/* faq & contact */
.block-title{position:absolute;top:2580px;font-family:var(--serif);font-size:31px;color:var(--ink);font-weight:400}
.faq-item{position:absolute;left:122px;width:477px;height:46px;border:1px solid var(--line);
  font-size:12px;color:#444;display:flex;align-items:center;padding-left:14px}
.faq-item::after{content:"";position:absolute;right:16px;top:20px;border:6px solid transparent;border-top-color:#aaa}
.field{position:absolute;left:651px;width:376px;border:1px solid var(--line);font-size:12px;color:#aaa;padding:14px 15px}

/* footer */
.site-footer{position:absolute;left:0;top:3035px;width:1200px;height:403px;background:var(--teal)}
.footer-brand{position:absolute;left:0;top:36px;width:1200px;text-align:center}
.footer-brand .brand-mark{width:46px;height:46px;border:2px solid var(--white);margin-bottom:6px}
.footer-brand .brand-name{color:var(--white);font-size:15px}
.contact-circle{position:absolute;top:141px;width:82px;height:82px;border:3px solid var(--white);border-radius:50%;display:flex;align-items:center;justify-content:center}
.contact-line{position:absolute;top:254px;width:260px;text-align:center;font-size:12.5px;color:var(--white)}
.social{position:absolute;top:3345px;width:32px;height:32px;border:1.5px solid var(--white);border-radius:50%}
.copyright{position:absolute;left:0;top:3438px;width:1200px;height:47px;background:var(--tan);
  display:flex;align-items:center;justify-content:center;font-size:12px;color:#4a3a2e}
</style>
</head>
<body>

<header class="site-header">
  <div class="brand"><span class="brand-mark"></span><span class="brand-name">STITCHWELL STUDIO</span></div>
  <nav class="main-nav">
    <a class="is-active" href="#">Home</a><a href="#">About</a><a href="#">Services</a><a href="#">Blogs</a><a href="#">Store Loctaion</a><a href="#">Contact</a>
  </nav>
  <div class="header-call">
    <svg width="30" height="30" viewBox="0 0 30 30"><circle cx="15" cy="15" r="13" fill="none" stroke="#222" stroke-width="2"/><path d="M10 8c1-1 2-1 3 1l1 3c0 1-1 1-1 2 1 2 2 3 4 4 1 0 1-1 2-1l3 1c2 1 2 2 1 3-2 2-5 2-8 0-3-2-5-4-6-7-1-2-1-4 1-6z" fill="#222"/></svg>
    <div class="header-call-text">ANY QUESTIONS?<span>+010 555 0147</span></div>
  </div>
</header>

<section class="hero">
  <div class="photo" role="img" aria-label="Close-up of hands guiding fabric through a sewing machine under warm light" style="inset:0"></div>
  <h1 class="hero-title">Get all your clothes<br>fitting better &amp; lasting longer!</h1>
  <a class="btn btn-tan" href="#" style="left:494px;top:369px;width:216px;height:50px">Make an appoinment</a>
  <svg class="hero-arrow" style="left:39px" width="48" height="48" viewBox="0 0 48 48"><circle cx="24" cy="24" r="22" fill="none" stroke="#fff" stroke-width="2"/><path d="M34 24H14M22 16l-8 8 8 8" fill="none" stroke="#fff" stroke-width="2"/></svg>
  <svg class="hero-arrow" style="left:1114px" width="48" height="48" viewBox="0 0 48 48"><circle cx="24" cy="24" r="22" fill="none" stroke="#fff" stroke-width="2"/><path d="M14 24h20M26 16l8 8-8 8" fill="none" stroke="#fff" stroke-width="2"/></svg>
  <div class="hero-dots"><i></i><i></i><i></i><i></i></div>
</section>

<section class="panel" style="top:745px;height:396px">
  <h2 class="panel-title" style="top:88px">About us</h2>
  <p class="panel-text" style="top:142px">Lorem Ipsum is simply dummy text of the printing and typesetting industry. Lorem Ipsum has been the industry's standard dummy text ever since the 1500s, when an unknown printer took a galley of type and scrambled it to make a type specimen book.</p>
  <a class="btn btn-white" href="#" style="left:124px;top:257px;width:170px;height:48px">Read more</a>
  <div class="photo" role="img" aria-label="Tailor's hands pinning grey suit fabric beside spools of thread" style="left:597px;top:0;width:603px;height:396px;background:linear-gradient(160deg,#e8e6e3,#a9a8ab 50%,#6c6d74)"></div>
</section>

<h2 class="services-heading">We offer a variety of services to<br>need your dry clean &amp; altration needs.</h2>
<a class="btn btn-teal" href="#" style="left:860px;top:1249px;width:217px;height:51px">Make an appoinment</a>

<div class="service" style="left:120px;top:1380px"><div class="service-icon" role="img" aria-label="Shirt and scissors icon"></div><h3 class="service-title">Clothing Alterations</h3><p class="service-text">Whether you want to shorten or restyle your clothes, we can make any alteration you need so you can finally feel completely comfortable in your clothes.</p></div>
<div class="service" style="left:369px;top:1380px"><div class="service-icon" role="img" aria-label="Folded jacket icon"></div><h3 class="service-title">Dry Cleaning</h3><p class="service-text">Entrust your delicate garment to us and we will make sure its professionally cleaned without risk of stretching or shrinkage.</p></div>
<div class="service" style="left:620px;top:1380px"><div class="service-icon" role="img" aria-label="Wedding gown icon"></div><h3 class="service-title">Wedding Dress Alterations</h3><p class="service-text">Our expert tailors will fit your wedding gown to your exact shape and size, so you'll look stunning on your special day.</p></div>
<div class="service" style="left:867px;top:1380px"><div class="service-icon" role="img" aria-label="Suit jacket icon"></div><h3 class="service-title">Suit Alterations</h3><p class="service-text">Make sure you always look professional and sharp with our suit alteration service. Our tailors will take care of everything and make certain they fit your unique shape and size.</p></div>

<div class="service" style="left:120px;top:1673px"><div class="service-icon" role="img" aria-label="Dress icon"></div><h3 class="service-title">Dress Alterations</h3><p class="service-text">Finding a dress that fits perfectly and creates a flattering look is difficult. Let us help you with our dress alterations, so you look your best with a dress which compliments your body.</p></div>
<div class="service" style="left:369px;top:1673px"><div class="service-icon" role="img" aria-label="Sewing machine icon"></div><h3 class="service-title">Dressmaking</h3><p class="service-text">Haven't found a dress you love for that special occasion? Fret no more, the BRIMFELT dressmakers can create a unique and glamorous look just for you.</p></div>
<div class="service" style="left:620px;top:1673px"><div class="service-icon" role="img" aria-label="Embroidery hoop icon"></div><h3 class="service-title">Embroidery</h3><p class="service-text">Create the perfect gift for your loved ones with our personalized embroidered gifts.Whether it's a baby blanket or a cushion or pillow, an embroidered gift will help you make an original &amp; unforgettable present.</p></div>
<div class="service" style="left:867px;top:1673px"><div class="service-icon" role="img" aria-label="Needle and patch icon"></div><h3 class="service-title">Invisible Mending</h3><p class="service-text">Have a valuable piece of clothing that needs a flawless fix? With our invisible mending we will take individual threads from the unseen interior of the garment and meticulously reweave it to the damaged areas.</p></div>

<section class="panel" style="top:2034px;height:456px">
  <div class="photo" role="img" aria-label="Man in a navy checked suit and blue tie in a dim shop, tinted teal" style="inset:0;background:linear-gradient(90deg,#16333b 0%,#17343c 45%,#2a4450 70%,#3a4f5e 85%,#1d3540 100%)"></div>
  <h2 class="panel-title" style="top:104px"><span style="font-size:62px;line-height:62px">O</span>ur Current Offers</h2>
  <p class="panel-text" style="top:186px">Lorem Ipsum is simply dummy text of the printing and typesetting industry. Lorem Ipsum has been the industry's standard dummy text ever since the 1500s, when an unknown printer took a galley of type and scrambled it to make a type specimen book.</p>
  <a class="btn btn-white" href="#" style="left:124px;top:303px;width:170px;height:48px">See offers</a>
</section>

<h2 class="block-title" style="left:119px">Frequently Ask Questions</h2>
<div class="faq-item" style="top:2653px">Lorem Ipsum is simply dummy text of the printing &amp; typesetting industry.</div>
<div class="faq-item" style="top:2702px">Lorem Ipsum is simply dummy text of the printing &amp; typesetting industry.</div>
<div class="faq-item" style="top:2752px">Lorem Ipsum is simply dummy text of the printing &amp; typesetting industry.</div>
<div class="faq-item" style="top:2801px">Lorem Ipsum is simply dummy text of the printing &amp; typesetting industry.</div>
<div class="faq-item" style="top:2851px">Lorem Ipsum is simply dummy text of the printing &amp; typesetting industry.</div>
<div class="faq-item" style="top:2903px">Lorem Ipsum is simply dummy text of the printing &amp; typesetting industry.</div>

<h2 class="block-title" style="left:759px">Contact us</h2>
<div class="field" style="top:2653px;height:46px">Full Name</div>
<div class="field" style="top:2702px;height:46px">Email address</div>
<div class="field" style="top:2752px;height:46px">Phone#</div>
<div class="field" style="top:2802px;height:98px">Message</div>
<a class="btn btn-teal" href="#" style="left:651px;top:2908px;width:376px;height:42px;border-radius:22px">Send now</a>

<footer class="site-footer">
  <div class="footer-brand"><span class="brand-mark"></span><span class="brand-name">STITCHWELL STUDIO</span></div>
  <div class="contact-circle" style="left:336px"><svg width="34" height="34" viewBox="0 0 30 30"><path d="M7 4c1.5-1.5 3-1 4 1l2 4c.5 1.5-1 2-1.5 3 1.5 3 3 4.5 6 6 1-.5 1.5-2 3-1.5l4 2c2 1 2.5 2.5 1 4-3 3-7 3-11 0s-7-6-9-10c-1-3-.5-6 1.5-8z" fill="#fff"/></svg></div>
  <div class="contact-circle" style="left:560px"><svg width="36" height="26" viewBox="0 0 36 26"><rect x="1" y="1" width="34" height="24" fill="none" stroke="#fff" stroke-width="2"/><path d="M1 1l17 13L35 1M1 25l12-12M35 25L23 13" fill="none" stroke="#fff" stroke-width="2"/></svg></div>
  <div class="contact-circle" style="left:786px"><svg width="26" height="34" viewBox="0 0 26 34"><path d="M13 1C6 1 1 6 1 13c0 8 12 20 12 20s12-12 12-20C25 6 20 1 13 1z" fill="#fff"/><circle cx="13" cy="13" r="4.5" fill="#16333b"/></svg></div>
  <div class="contact-line" style="left:248px">+010 555 0147</div>
  <div class="contact-line" style="left:471px">hello@stitchwellstudio.example</div>
  <div class="contact-line" style="left:697px">18 Thimble Lane, Harrowfield 04410</div>
</footer>
<span class="social" style="left:514px" aria-label="Social link"></span>
<span class="social" style="left:562px" aria-label="Social link"></span>
<span class="social" style="left:608px" aria-label="Social link"></span>
<span class="social" style="left:655px" aria-label="Social link"></span>
<div class="copyright">Copyright © 2019. Stitchwell Studio- All right reserved.</div>

</body>
</html>
```